11 x 11 Flyer Design for Social Media - Reverse Mortgages

62 or older?

A Reverse Mortgage
could be
Your Road to Financial Freedom

* No Monthly Payments
* No Income Requirements
* No Credit Score Requirements
* No Loss of Ownership

Receive cash by lump sum, monthly installments or a line of credit!!

Call us today for a Free Consultation!!
(800) 471-2965

Bluegate Financial Services, Inc.
NMLS #318760
www.bluegatehome.com

```html
<!DOCTYPE html>
<html lang="en">
<head>
<meta charset="utf-8">
<title>Reverse Mortgage Flyer – Bluegate Financial Services</title>
<link rel="stylesheet" href="https://fonts.googleapis.com/css2?family=Libre+Baskerville:wght@400;700&family=Roboto+Condensed:wght@700&display=swap">
<style>
  :root {
    --stage: #4d4d4d;
    --paper: #ffffff;
    --gold: #a08b2c;
    --blue: #0b4f91;
    --ink: #1b1b1b;
    --band: #0d4f8e;
    --photo-warm: #e8c9b4;
    --photo-cool: #dfe6ef;
  }
  * { box-sizing: border-box; margin: 0; padding: 0; }
  html, body { width: 1200px; height: 900px; overflow: hidden; }
  body {
    background: var(--stage);
    font-family: "Libre Baskerville", Georgia, serif;
    color: var(--ink);
    position: relative;
  }
  .flyer {
    position: absolute; left: 228px; top: 58px;
    width: 750px; height: 750px;
    background: var(--paper);
    overflow: hidden;
  }
  .flyer > * { position: absolute; }

  .house-photo {
    left: 330px; top: 120px; width: 420px; height: 440px;
    background: radial-gradient(ellipse at 62% 55%, var(--photo-warm) 0%, #c9a99a 22%, #d8dde6 48%, rgba(255,255,255,0) 72%);
  }
  .brand {
    left: 500px; top: 70px; width: 220px;
    display: flex; align-items: center; gap: 10px;
    font-weight: 700; font-size: 15px; line-height: 1.3; color: var(--blue);
  }
  .brand-dot { width: 26px; height: 26px; border-radius: 50%; background: var(--gold); flex: none; }

  .headline {
    left: 0; width: 410px; top: 52px; text-align: center;
    font-weight: 700; font-size: 74px; line-height: 1.02;
  }
  .headline .line-gold { color: var(--gold); display: block; }
  .headline .line-blue { color: var(--blue); display: block; margin-top: 2px; }

  .subhead {
    left: 0; width: 404px; top: 222px; text-align: center;
    font-weight: 700; font-size: 17px; line-height: 1.35; color: var(--ink);
  }

  .benefits { left: 42px; top: 290px; list-style: none; }
  .benefit {
    position: relative; height: 46px; margin-bottom: 10px;
    display: flex; align-items: center;
  }
  .benefit-pill {
    margin-left: 30px; height: 46px; padding: 0 24px 0 27px;
    display: flex; align-items: center;
    border: 2px solid var(--gold); border-left: none;
    border-radius: 0 23px 23px 0;
    font-size: 18px; color: var(--ink);
  }
  .benefit:nth-child(even) .benefit-pill { border-color: var(--blue); }
  .benefit-tick {
    position: absolute; left: 0; top: 0;
    width: 46px; height: 46px; border-radius: 50%;
    background: var(--blue);
    display: flex; align-items: center; justify-content: center;
  }
  .benefit:nth-child(even) .benefit-tick { background: var(--gold); }

  .cash-band {
    left: 0; top: 558px; width: 750px; height: 60px;
    background: var(--band);
  }
  .band-shadow {
    left: 230px; top: 618px; width: 520px; height: 40px;
    background: linear-gradient(180deg, #e4e4e4, rgba(255,255,255,0));
    clip-path: polygon(0 0, 100% 0, 100% 40%, 50% 100%, 0 40%);
  }

  .couple-photo {
    left: 42px; top: 522px; width: 220px; height: 228px;
    background: linear-gradient(180deg, #6b4a38 0%, #8a6550 35%, #f1f1f1 60%, #e6e6e6 100%);
    border-radius: 100px 100px 0 0;
  }

  .cash-text {
    left: 262px; top: 569px; width: 440px; text-align: center;
    color: #fff; font-weight: 700; font-size: 15.5px; line-height: 1.35;
    z-index: 2;
  }

  .call {
    left: 298px; top: 653px; width: 200px; text-align: center;
    font-weight: 700; font-size: 12.5px; line-height: 1.4;
  }
  .call-phone {
    display: block; margin-top: 2px;
    font-family: "Roboto Condensed", Arial, sans-serif;
    font-size: 25px; color: var(--blue); letter-spacing: 0.3px;
  }
  .divider { left: 498px; top: 654px; width: 1px; height: 58px; background: #bbb; }
  .company {
    left: 522px; top: 658px;
    font-weight: 700; font-size: 12.5px; line-height: 1.33;
  }
</style>
</head>
<body>
  <main class="flyer">
    <div class="house-photo" role="img" aria-label="Photo of a small model house with a dark tiled roof on financial papers"></div>

    <div class="brand"><span class="brand-dot"></span><span>Bluegate Financial Services, Inc.</span></div>

    <h1 class="headline"><span class="line-gold">62 OR</span><span class="line-blue">OLDER?</span></h1>

    <p class="subhead">A REVERSE MORTGAGE COULD BE<br>Your Road to Financial Freedom</p>

    <ul class="benefits">
      <li class="benefit"><span class="benefit-tick"><svg width="26" height="26" viewBox="0 0 26 26"><polyline points="4,14 10,21 22,5" fill="none" stroke="#fff" stroke-width="4" stroke-linecap="round" stroke-linejoin="round"/></svg></span><span class="benefit-pill">No Monthly Payments</span></li>
      <li class="benefit"><span class="benefit-tick"><svg width="26" height="26" viewBox="0 0 26 26"><polyline points="4,14 10,21 22,5" fill="none" stroke="#fff" stroke-width="4" stroke-linecap="round" stroke-linejoin="round"/></svg></span><span class="benefit-pill">No Income Requirements</span></li>
      <li class="benefit"><span class="benefit-tick"><svg width="26" height="26" viewBox="0 0 26 26"><polyline points="4,14 10,21 22,5" fill="none" stroke="#fff" stroke-width="4" stroke-linecap="round" stroke-linejoin="round"/></svg></span><span class="benefit-pill">No Credit Score Requirements</span></li>
      <li class="benefit"><span class="benefit-tick"><svg width="26" height="26" viewBox="0 0 26 26"><polyline points="4,14 10,21 22,5" fill="none" stroke="#fff" stroke-width="4" stroke-linecap="round" stroke-linejoin="round"/></svg></span><span class="benefit-pill">No Loss of Ownership</span></li>
    </ul>

    <div class="cash-band"></div>
    <div class="band-shadow"></div>

    <div class="couple-photo" role="img" aria-label="Photo of a smiling senior couple in white shirts"></div>

    <p class="cash-text">Receive cash by lump sum, monthly installments<br>or a line of credit!!</p>

    <p class="call">Call us today for a<br>FREE CONSULTATION!!<span class="call-phone">(800) 471-2965</span></p>
    <div class="divider"></div>
    <p class="company">Bluegate Financial Services, Inc.<br>NMLS #318760<br>www.bluegatehome.com</p>
  </main>
</body>
</html>
```